IT Company Business Card design

Brisk Loop is a new computer solutions business focusing on setting up servers and computer systems for small to medium sized businesses.

A business client will either request a solution, or support for a current system and we will turn up on site to provide these services.

We are bast in Christchurch, New Zealand.

We are looking for unique business card's that stand out and show off the business in a professional light.

Open to all idea's etc.

Industry/Entity Type

Computer

Requirements
Must have
• Business Logo (AI file attached)
Employee Name
Business title
Business landline number
Cell phone number
Email
Web URL
Nice to have
• Could be nice to have some keywords (possibly on the back) such as:

Business IT solutions
Network installations
Phone solutions
Server management
Software diagnostics

The above is not needed, just an idea.

```html
<!DOCTYPE html>
<html lang="en">
<head>
<meta charset="utf-8">
<title>Brisk Loop – Business Card</title>
<link rel="stylesheet" href="https://fonts.googleapis.com/css2?family=Jost:wght@400&family=Tinos:wght@400;700&display=swap">
<style>
  :root {
    --backdrop: #8b8e87;
    --card-silver-light: #e4e3df;
    --card-silver-dark: #c9c7c1;
    --band-glow: #08b6f2;
    --band-mid: #1166c8;
    --band-deep: #15207a;
    --accent-line: #2fb8f0;
    --ink: #141414;
    --paper-text: #ffffff;
    --mark-blue: #1a78d4;
  }
  * { box-sizing: border-box; margin: 0; padding: 0; }
  html, body { width: 1200px; height: 1189px; overflow: hidden; }
  body { background: var(--backdrop); position: relative; }

  .card {
    position: absolute;
    left: 167px;
    width: 867px;
    height: 495px;
    border-radius: 20px;
    overflow: hidden;
    background: linear-gradient(180deg, var(--card-silver-light) 0%, var(--card-silver-dark) 100%);
    box-shadow: 0 2px 10px rgba(0,0,0,0.25);
  }
  .card--front { top: 61px; }
  .card--back { top: 632px; }

  .brand { position: absolute; left: 177px; top: 28px; height: 160px; display: flex; align-items: center; }
  .brand__dot { width: 160px; height: 160px; border-radius: 50%; background: var(--mark-blue); flex: none; }
  .brand__name {
    margin-left: 45px;
    font-family: "Jost", sans-serif;
    font-weight: 400;
    font-size: 60px;
    letter-spacing: 0.08em;
    color: var(--ink);
    text-transform: uppercase;
    white-space: nowrap;
  }

  .band {
    position: absolute;
    left: 0; right: 0;
    top: 219px;
    height: 246px;
    background: radial-gradient(ellipse 60% 85% at 40% 45%, var(--band-glow) 0%, var(--band-mid) 45%, var(--band-deep) 100%);
    border-top: 3px solid var(--accent-line);
  }
  .band::after {
    content: "";
    position: absolute;
    left: 0; right: 0; bottom: 3px;
    height: 2px;
    background: var(--accent-line);
  }
  .band__pointer {
    position: absolute;
    left: 148px; top: -1px;
    width: 0; height: 0;
    border-left: 24px solid transparent;
    border-right: 24px solid transparent;
    border-top: 26px solid #0c0c14;
  }

  .person {
    position: absolute;
    left: 72px; top: 34px;
    width: 200px;
    text-align: center;
    color: var(--paper-text);
    font-family: "Tinos", serif;
    line-height: 31px;
  }
  .person__name { font-weight: 700; font-size: 25px; }
  .person__title { font-weight: 400; font-size: 25px; }

  .band__divider {
    position: absolute;
    left: 429px; top: 20px;
    width: 2px; height: 208px;
    background: linear-gradient(180deg, rgba(255,255,255,0.1), rgba(255,255,255,0.75), rgba(255,255,255,0.1));
  }

  .contact {
    position: absolute;
    left: 456px; top: 24px;
    color: var(--paper-text);
    font-family: "Tinos", serif;
    font-size: 26px;
    line-height: 31.5px;
    list-style: none;
  }
  .contact li { display: flex; align-items: center; white-space: nowrap; }
  .contact__icon { width: 19px; height: 19px; margin-right: 6px; flex: none; fill: none; stroke: var(--paper-text); stroke-width: 1.8; }
  .contact__icon--solid { fill: var(--paper-text); stroke: none; }

  .site-line {
    position: absolute;
    left: 0; right: 0; top: 105px;
    text-align: center;
    color: var(--paper-text);
    font-family: "Tinos", serif;
    font-size: 30px;
    letter-spacing: 0.75em;
    padding-left: 0.75em;
    white-space: nowrap;
  }
</style>
</head>
<body>

  <section class="card card--front" aria-label="Business card front">
    <div class="brand">
      <span class="brand__dot"></span>
      <span class="brand__name">Brisk Loop</span>
    </div>
    <div class="band">
      <span class="band__pointer"></span>
      <div class="person">
        <p class="person__name">Sample Name</p>
        <p class="person__title">S.E.O</p>
      </div>
      <span class="band__divider"></span>
      <ul class="contact">
        <li>Address Kestrel Bay,</li>
        <li>Northvale.</li>
        <li>
          <svg class="contact__icon" viewBox="0 0 20 20"><path d="M14 3c-4 1-8 6-8 11 0 2 1 3 2 3" stroke-linecap="round"/><path class="contact__icon--solid" d="M12 2l4 0 0 3-4 1z M6 15l3 1-1 3-3-1z"/></svg>
          (111) 111-111
        </li>
        <li>
          <svg class="contact__icon" viewBox="0 0 20 20"><rect x="5" y="1.5" width="10" height="17" rx="1.5"/><rect x="7" y="4" width="6" height="6"/></svg>
          (111) 111-111
        </li>
        <li>
          <svg class="contact__icon" viewBox="0 0 20 20"><rect x="1.5" y="5" width="17" height="11"/><path d="M1.5 5l8.5 6 8.5-6"/></svg>
          sample@briskloop.co.nz
        </li>
        <li>
          <svg class="contact__icon" viewBox="0 0 20 20"><circle cx="10" cy="10" r="7.5"/><path d="M2.5 10h15M10 2.5v15M4.5 6h11M4.5 14h11"/></svg>
          www.briskloop.co.nz
        </li>
      </ul>
    </div>
  </section>

  <section class="card card--back" aria-label="Business card back">
    <div class="brand">
      <span class="brand__dot"></span>
      <span class="brand__name">Brisk Loop</span>
    </div>
    <div class="band">
      <p class="site-line">www.briskloop.co.nz</p>
    </div>
  </section>

</body>
</html>
```